Korvane Pty Ltd professional business card

A professional business card template using the colours from the supplied logo.
Clean crisp lines while, Modern while not being over the top.

Target Market(s)

Construction, commerical and industrial

Industry/Entity Type

Communications

Contact Information for Business Card

For a Communications, IT, Optical fibre installation company

Colors
37b8a4

```html
<!DOCTYPE html>
<html lang="en">
<head>
<meta charset="UTF-8">
<title>Korvane Pty Ltd — Business Card</title>
<link href="https://fonts.googleapis.com/css2?family=Roboto:wght@400;500&display=swap" rel="stylesheet">
<style>
  :root {
    --teal: #2a939c;
    --ink: #5f6166;
    --ink-soft: #7a7c80;
    --paper: #ffffff;
    --slate: #2e2f31;
    --slate-mark: #4a4b4e;
    --backdrop: #e6e6e4;
    --divider: #9a9ca0;
  }
  * { box-sizing: border-box; margin: 0; padding: 0; }
  html, body { width: 1200px; height: 801px; overflow: hidden; }
  body {
    background: var(--backdrop);
    font-family: "Roboto", Arial, sans-serif;
    display: flex;
    align-items: center;
    justify-content: center;
    gap: 48px;
  }
  .card {
    width: 530px;
    height: 303px;
    position: relative;
    border-bottom: 4px solid var(--teal);
    box-shadow: 0 10px 24px rgba(0,0,0,0.12);
  }
  .card--front { background: var(--paper); }
  .card--back {
    background: var(--slate);
    display: flex;
    align-items: center;
    justify-content: center;
  }
  .front-main {
    position: absolute;
    left: 62px;
    top: 78px;
    display: flex;
    align-items: center;
  }
  .identity { width: 200px; }
  .wordmark {
    display: flex;
    align-items: center;
    gap: 8px;
    font-size: 38px;
    font-weight: 500;
    letter-spacing: 1px;
    color: var(--ink);
    margin-bottom: 20px;
  }
  .wordmark__dot {
    width: 16px; height: 16px;
    border-radius: 50%;
    background: var(--teal);
  }
  .person__name {
    font-size: 20px;
    font-weight: 500;
    color: var(--teal);
    line-height: 1.1;
  }
  .person__role {
    font-size: 15px;
    color: var(--ink-soft);
    margin-top: 2px;
  }
  .divider {
    width: 1px;
    height: 84px;
    background: var(--divider);
    margin: 0 22px 0 8px;
    align-self: flex-end;
  }
  .contacts {
    list-style: none;
    font-size: 14px;
    color: var(--ink);
    align-self: flex-end;
  }
  .contacts li {
    display: flex;
    align-items: center;
    gap: 9px;
    line-height: 24px;
  }
  .contacts svg { width: 12px; height: 12px; flex: none; }
  .contacts .accent { color: var(--teal); }
  .address {
    position: absolute;
    left: 62px;
    right: 40px;
    bottom: 52px;
    text-align: right;
    font-size: 14px;
    color: var(--ink-soft);
  }
  .back-mark {
    display: flex;
    align-items: center;
    gap: 14px;
    font-size: 72px;
    font-weight: 500;
    letter-spacing: 2px;
    color: var(--slate-mark);
  }
  .back-mark__dot {
    width: 26px; height: 26px;
    border-radius: 50%;
    background: var(--slate-mark);
  }
</style>
</head>
<body>
  <section class="card card--front">
    <div class="front-main">
      <div class="identity">
        <div class="wordmark"><span class="wordmark__dot"></span>KORVANE</div>
        <div class="person">
          <p class="person__name">Marcus Hale</p>
          <p class="person__role">Manager</p>
        </div>
      </div>
      <div class="divider"></div>
      <ul class="contacts">
        <li>
          <svg viewBox="0 0 12 12" aria-hidden="true"><path d="M3 1l2 2.4-1.2 1.2a7 7 0 0 0 3.6 3.6L8.6 7 11 9l-1.4 2C5 11 1 7 1 2.4z" fill="var(--teal)"/></svg>
          555-014-2100
        </li>
        <li>
          <svg viewBox="0 0 12 12" aria-hidden="true"><rect x="1" y="2.5" width="10" height="7" fill="none" stroke="var(--teal)" stroke-width="1.2"/><path d="M1 2.5l5 4 5-4" fill="none" stroke="var(--teal)" stroke-width="1.2"/></svg>
          name@korvanemail.com
        </li>
        <li>
          <svg viewBox="0 0 12 12" aria-hidden="true"><circle cx="6" cy="6" r="5" fill="var(--teal)"/><path d="M1 6h10M6 1c-2.5 3-2.5 7 0 10M6 1c2.5 3 2.5 7 0 10" fill="none" stroke="#fff" stroke-width="0.8"/></svg>
          <span>www.<span class="accent">korvanesite</span>.com</span>
        </li>
      </ul>
    </div>
    <p class="address">Your address, city, state, ZIP 0000</p>
  </section>

  <section class="card card--back">
    <div class="back-mark"><span class="back-mark__dot"></span>KORVANE</div>
  </section>
</body>
</html>
```